Etiketten für Honiggläser gesucht
sehr kreativer Entwurf, in dem alle umfangreichen Vorgaben berücksichtigt wurden. q4712 ist sehr service- und lösungsorientiert. Arbeitet sehr schnell und exzellent.
Zielgruppe
Wir sind eine junge Hobbyimkerei und produzieren unsere eigenen Honigsorten. Zielgruppe ist jeder, der Honig mag.
Aufgabenstellung
Das zu entwerfende Etiketten_Design soll grundsätzlich ein „absoluter Hingucker“ werden, einen hohen Wiedererkennungswert besitzen, edel erscheinen und die Hochwertigkeit des Produktes zum Ausdruck bringen.
Im engeren Sinn sollen zwei voneinander unabhängige Etikettenteile entworfen werden, die aber im Design eine Einheit bilden sollen:
Beim ersten Teil handelt es sich um den sogenannten Gewährverschluss; er verbindet den Deckel mit dem Glas und zerreißt beim ersten Öffnen des Deckels. Der Gewährverschluss soll etwa 2 cm breit und 8 cm lang sein, und unter anderem von unserem Firmenlogo (siehe Datei) geziert werden. Bei dem Logo darf die Grafik und der Hintergrund in der Farbe variieren, und der Schriftzug kann entfallen, andere Änderungen dürfen jedoch nicht vorgenommen werden. Das Logo kann bei Bedarf gerne in anderen Dateiformaten zur Verfügung gestellt werden.
Den zweiten Teil stellt das eigentliche Produktetikett dar. Für dieses gibt es keine Größen- und Formvorgaben, allerdings müssen folgende Inhalte Berücksichtigung finden: Die Daten des Imkers (bitte folgende Platzhalter verwenden „Firmenname“, „Vorname1 & Vorname2 Nachname“, „Straße + Hausnummer“, „PLZ + Ortsname“, „Internetseite“ und „Emailadresse“) sowie den Angaben „500g“, „Mindestens haltbar bis:“ (dahinter oder darunter bitte weißen Freiraum für den Stempelaufdruck des Datums lassen), „Trocken, dunkel und vor Wärme geschützt lagern!“, und – ganz wichtig – die „Honigsorte“ mit den vorangestellten Worten „feinster deutscher“ (, z.B. „feinster deutscher Rapshonig“).
Jede Honigsorte soll mit einer Farbe verknüpft werden, sodass der Kunde schnell erkennen kann um welche Honigsorte es sich im Glas handelt (beispielsweise gelb für Rapshonig, grün für Waldhonig, usw.). Dafür soll die jeweilige Honigsortenfarbe, in welcher Form auch immer, das Etikett oder einen bestimmten Bereich davon domini..

```html
<!DOCTYPE html>
<html lang="de">
<head>
<meta charset="utf-8">
<title>Imkerei Lindhoff – Honigetiketten</title>
<link rel="stylesheet" href="https://fonts.googleapis.com/css2?family=Dancing+Script:wght@500&family=Marcellus&family=Open+Sans:wght@600;700&family=Rajdhani:wght@500&display=swap">
<style>
  :root {
    --paper: #ffffff;
    --ink: #222222;
    --ring: #2b2b2b;
    --address: #555555;
    --wood: #6b4a22;
    --seal: #1c1c1c;
    --forest: #4a8f5e;
    --forest-deep: #0c9444;
    --raspberry: #c21d48;
  }
  html, body { margin: 0; padding: 0; overflow: hidden; background: var(--paper); }
  .canvas { display: block; width: 1200px; height: 848px; }
  .address-ring { font-family: "Open Sans", sans-serif; font-weight: 700; font-size: 10.5px; fill: var(--address); letter-spacing: 0.3px; }
  .variety { font-family: "Dancing Script", cursive; font-weight: 500; font-size: 25px; }
  .brand-top { font-family: "Marcellus", serif; font-size: 21px; letter-spacing: 8px; fill: var(--ink); }
  .brand-name { font-family: "Marcellus", serif; font-size: 29px; letter-spacing: 2px; fill: var(--ink); font-weight: 700; }
  .weight { font-family: "Rajdhani", sans-serif; font-weight: 500; font-size: 16px; fill: var(--paper); }
  .storage { font-family: "Open Sans", sans-serif; font-weight: 600; font-size: 5.6px; fill: var(--paper); }
  .best-before { font-family: "Open Sans", sans-serif; font-weight: 700; font-size: 4.8px; fill: var(--paper); }
  .label--forest .variety { fill: var(--forest); }
  .label--raspberry .variety { fill: var(--raspberry); }
</style>
</head>
<body>
<svg class="canvas" viewBox="0 0 1200 848" xmlns="http://www.w3.org/2000/svg">
  <defs>
    <path id="address-arc" d="M -134.9 23.8 A 137 137 0 1 1 134.9 23.8"/>
    <path id="variety-arc" d="M -129.7 47.2 A 138 138 0 0 0 129.7 47.2"/>
    <linearGradient id="forest-fill" x1="0" x2="1" y1="0" y2="0">
      <stop offset="0" stop-color="var(--forest-deep)"/>
      <stop offset="0.35" stop-color="var(--forest)"/>
      <stop offset="1" stop-color="var(--forest)"/>
    </linearGradient>
  </defs>

  <g class="seal-strip">
    <path d="M184 126 H248 V330 L216 306 L184 330 Z" fill="var(--seal)"/>
  </g>

  <g class="label label--forest" transform="translate(619 345)">
    <g class="label-ribbon">
      <path d="M-41 140 H41 V351 L0 321 L-41 351 Z" fill="url(#forest-fill)"/>
      <text class="weight" x="0" y="197" text-anchor="middle">500G.</text>
      <text class="storage" x="0" y="209" text-anchor="middle">Trocken, dunkel und vor</text>
      <text class="storage" x="0" y="216.5" text-anchor="middle">Wärme geschützt lagern</text>
      <text class="best-before" x="0" y="228" text-anchor="middle">Mindestens haltbar bis:</text>
      <rect x="-35" y="234" width="70" height="15" fill="var(--paper)"/>
      <circle cx="0" cy="280" r="14" fill="none" stroke="var(--paper)" stroke-width="1.2"/>
    </g>
    <circle r="171" fill="url(#forest-fill)"/>
    <circle r="161" fill="var(--paper)"/>
    <circle r="152" fill="none" stroke="var(--ring)" stroke-width="3.5"/>
    <text class="address-ring"><textPath href="#address-arc" startOffset="50%" text-anchor="middle">Moosweg 14 • 3012 Talheim • www.imkereilindhoff.de • kontakt@imkereilindhoff.de</textPath></text>
    <circle class="brand-mark" cx="0" cy="-48" r="42" fill="none" stroke="var(--wood)" stroke-width="3"/>
    <text class="brand-top" x="4" y="42" text-anchor="middle">IMKEREI</text>
    <text class="brand-name" x="0" y="76" text-anchor="middle">LINDHOFF</text>
    <text class="variety"><textPath href="#variety-arc" startOffset="50%" text-anchor="middle">Feinster Deutscher Waldhonig</textPath></text>
  </g>

  <g class="label label--raspberry" transform="translate(1007 339)">
    <g class="label-ribbon">
      <path d="M-40 140 H40 V350 L0 320 L-40 350 Z" fill="var(--raspberry)"/>
      <text class="weight" x="0" y="197" text-anchor="middle">500G.</text>
      <text class="storage" x="0" y="209" text-anchor="middle">Trocken, dunkel und vor</text>
      <text class="storage" x="0" y="216.5" text-anchor="middle">Wärme geschützt lagern</text>
      <text class="best-before" x="0" y="228" text-anchor="middle">Mindestens haltbar bis:</text>
      <rect x="-34" y="234" width="68" height="15" fill="var(--paper)"/>
      <circle cx="0" cy="279" r="14" fill="none" stroke="var(--paper)" stroke-width="1.2"/>
    </g>
    <circle r="169" fill="var(--raspberry)"/>
    <circle r="160" fill="var(--paper)"/>
    <circle r="151" fill="none" stroke="var(--ring)" stroke-width="3.5"/>
    <text class="address-ring"><textPath href="#address-arc" startOffset="50%" text-anchor="middle">Moosweg 14 • 3012 Talheim • www.imkereilindhoff.de • kontakt@imkereilindhoff.de</textPath></text>
    <circle class="brand-mark" cx="0" cy="-48" r="42" fill="none" stroke="var(--wood)" stroke-width="3"/>
    <text class="brand-top" x="4" y="42" text-anchor="middle">IMKEREI</text>
    <text class="brand-name" x="0" y="76" text-anchor="middle">LINDHOFF</text>
    <text class="variety"><textPath href="#variety-arc" startOffset="50%" text-anchor="middle">Feinster Deutscher Himbeerhonig</textPath></text>
  </g>
</svg>
</body>
</html>
```